Rondo Brisk Painting, Eco and Non toxic painting client information brochure.

Rondo brisk painting is a painting company that specialises in eco and non toxic paints. This brochure will be left with the client after the initial meeting to explain about my business and hopefully win the job. By reading the text i have provided (see attachment) you can get a better understanding of what we do.
The brochure should be fresh and clean looking, complimenting the Rondo Brisk Painting logo and the text provided.
This will be printed onto a recycled paper.
Text and font must clear and easy to read.

Please have a look at my web page. I will be redoing this soon as well but this will give you some ideas of where I'm at.

Would like some picture but not sure what.
I have attached some pics but they don't have to be use

Hi peeps,

Thanks for all the great designs and sorry i haven't got back to you sooner.
been a bit busy.
Tomorrow i hope to be able to sit down and have a good look at what everybody has done.
Thanks again i really appreciate the effort.

kind regards gerald 

hi designers,

Just sat down and had a good look at the designs sent in and there are some crackers.
Its going to be very difficult to choose. I have only 1 day left before it closes so ill wait till then to see if there are any more submissions come in then ill get back to everybody.
Thanks again for your time and effort.

kind regards gerald 

Hi too all you designers that have worked on my project. 

I am always amazed at all the different designs that come through. Super work guys and girls. 
I have narrowed it down to a couple of designs.
Ill be making the decision tonight.
Thanks again to you all and i really appreciate all the hard work.
I will be doing another brochure in the future for more architecture / builder focus and there were a few designs that would work perfectly for this.

Kinds regards gerald  

Target Market(s)

The work we do is mainly residential repaints, family homes
Mostly I am dealing with the wife of the family or female designers/architects

Industry/Entity Type

Painting

Requirements
Must have
• Company logo, either white or black version what ever suits best.
Text that has been provided.
Brochure will be 1 page A 4, folded into 3 parts both sides.
Front page must have logo and
SPECIALSING IN:
NON TOXIC
ECO FRIENDLY &
HEAT REFLECTIVE PAINTS
Phone 041 862 9147
Painting@rondobrisk.biz
www.rondobrisk.biz

```html
<!DOCTYPE html>
<html lang="en">
<head>
<meta charset="utf-8">
<title>Rondo Brisk Painting – Client Information</title>
<link rel="stylesheet" href="https://fonts.googleapis.com/css2?family=Exo+2:wght@700;800&family=Ubuntu:wght@400;700&display=swap">
<style>
  :root {
    --sky-deep: #2f6fc4;
    --sky-mid: #6fa6e2;
    --sky-pale: #d9e9f8;
    --paper: #ffffff;
    --meadow: #e3efb4;
    --meadow-soft: #f4f8e4;
    --leaf: #4ea42a;
    --leaf-dark: #2f7d18;
    --leaf-light: #8cc63f;
    --lime-wall: #b9d62c;
    --lime-wall-light: #d7e85a;
    --sun-wall: #f2c20f;
    --sun-wall-light: #f8dc4a;
    --text: #4a4a4a;
    --pill-text: #ffffff;
  }
  * { margin: 0; padding: 0; box-sizing: border-box; }
  html, body { width: 1200px; height: 848px; overflow: hidden; }
  body { font-family: "Ubuntu", Arial, sans-serif; color: var(--text); background: var(--paper); }

  .brochure-panel {
    position: relative;
    width: 1200px;
    height: 848px;
    overflow: hidden;
    background: linear-gradient(180deg, var(--paper) 0%, var(--paper) 52%, var(--meadow-soft) 72%, var(--meadow) 100%);
  }

  .sky-banner {
    position: absolute; left: 0; top: 0; width: 1200px; height: 215px;
    background:
      radial-gradient(ellipse 70% 60% at 50% 100%, rgba(255,255,255,1) 35%, rgba(255,255,255,0) 70%),
      linear-gradient(180deg, var(--sky-deep) 0%, var(--sky-mid) 40%, var(--sky-pale) 70%, var(--paper) 100%);
  }

  .foliage {
    position: absolute; bottom: 0; height: 190px;
    background: radial-gradient(ellipse at 50% 80%, rgba(78,164,42,.55) 0%, rgba(140,198,63,.25) 45%, rgba(140,198,63,0) 70%);
  }
  .foliage--left { left: -40px; width: 300px; }
  .foliage--right { right: -30px; width: 260px; }

  .section-pill {
    position: absolute;
    height: 29px;
    padding: 0 14px;
    border-radius: 14px;
    border: 2px solid var(--paper);
    box-shadow: 0 0 0 1.5px var(--leaf), 0 2px 3px rgba(0,0,0,.2);
    background: linear-gradient(180deg, var(--leaf-light) 0%, var(--leaf) 55%, var(--leaf-dark) 100%);
    font-family: "Exo 2", Arial, sans-serif;
    font-weight: 800;
    font-size: 15px;
    letter-spacing: .5px;
    line-height: 25px;
    text-transform: uppercase;
    color: var(--pill-text);
  }

  .body-copy {
    position: absolute;
    font-size: 13.4px;
    line-height: 20.5px;
  }
  .body-copy p + p { margin-top: 9px; }
  .body-copy strong { font-weight: 700; }

  .about-business-title { left: 36px; top: 161px; width: 214px; }
  .about-business-copy { left: 51px; top: 198px; width: 332px; }

  .about-owner-title { left: 425px; top: 216px; width: 213px; }
  .about-owner-copy { left: 443px; top: 252px; width: 338px; }

  .hiring-title { left: 809px; top: 216px; width: 230px; }
  .hiring-copy { left: 826px; top: 252px; width: 346px; }

  .going-green-title { left: 425px; top: 667px; width: 213px; }
  .going-green-copy { left: 443px; top: 702px; width: 495px; }

  .interior-frame {
    position: absolute; left: 402px; top: 356px; width: 798px; height: 290px;
    background: linear-gradient(180deg, var(--leaf-light), var(--leaf));
    clip-path: polygon(0 0, 100% 0, 100% 100%, 42px 100%, 0 calc(100% - 42px));
  }
  .interior-photo {
    position: absolute; left: 412px; top: 368px; width: 774px; height: 262px;
    display: flex;
    border: 2px solid var(--paper);
  }
  .interior-photo__wall--lime {
    width: 395px;
    background: linear-gradient(180deg, var(--lime-wall) 0%, var(--lime-wall-light) 55%, #e9ecd8 100%);
  }
  .interior-photo__wall--sun {
    flex: 1;
    background: radial-gradient(ellipse 45% 50% at 40% 35%, #fff6a0 0%, var(--sun-wall-light) 40%, var(--sun-wall) 80%), var(--sun-wall);
  }
</style>
</head>
<body>
<main class="brochure-panel">
  <div class="sky-banner" role="img" aria-label="Blue sky with sun rays and soft white clouds"></div>
  <div class="foliage foliage--left" role="img" aria-label="Fresh green leaves"></div>
  <div class="foliage foliage--right" role="img" aria-label="Fresh green leaves"></div>

  <h2 class="section-pill about-business-title">About the Business</h2>
  <div class="body-copy about-business-copy">
    <p>At Rondo Brisk Painting we provide a high-quality service and exceptional craftsmanship for both domestic and commercial projects. We are proud to say we are making our work practices and business support processes more sustainable. We want to be sure we are doing our part to reduce our carbon footprint.</p>
    <p>We take the time to research alternative eco painting products and processes. We can also provide you with information about the products and why we use them. All our jobs are professionally finished utilising only the best tools and products available.</p>
    <p>We aim to limit the interruption to clients and their families as a result of our work; safety is paramount. We make sure that you are satisfied with the work done and will communicate with you throughout the job.</p>
    <p><strong>Rondo Brisk Painting</strong> is dedicated to learning, understanding and implementing new products and techniques that will be safer for the environment and your family. All this is done at a competitive price</p>
  </div>

  <h2 class="section-pill about-owner-title">About the Owner</h2>
  <div class="body-copy about-owner-copy">
    <p>Gerald Brisk has been painting for over 20 years. He is an accredited Green Painter and is often called upon by architects and builders to provide advice on sustainable products and methods.</p>
  </div>

  <h2 class="section-pill hiring-title">Hiring a Professional</h2>
  <div class="body-copy hiring-copy">
    <p>Hiring a professional painter is never an easy decision and should not be taken lightly. Painting is a highly skilled trade and it takes considerable experience and expertise to obtain a high quality finish.</p>
  </div>

  <div class="interior-frame"></div>
  <div class="interior-photo" role="img" aria-label="Freshly painted living room with a lime green wall, white sofa and shelf, and a warm yellow wall with pendant lamp, low cabinet and armchair">
    <div class="interior-photo__wall--lime"></div>
    <div class="interior-photo__wall--sun"></div>
  </div>

  <h2 class="section-pill going-green-title">Going Green</h2>
  <div class="body-copy going-green-copy">
    <p>We can help you make smart decisions about creating a better environment and further minimizing any risk for your family and the spaces we live in. This can be achieved reducing the amount of VOCs (volatile organic compounds) by selecting the correct products.</p>
  </div>
</main>
</body>
</html>
```